Business card por a urban DJ, up scale audience target

Need a sober design, modern, conservative colors but i can consider some options, y play rnb, hip hop, EDM and top40.

Business card for contact and personal info, double sided, use logo attrached please; im 42 so i need a card acording to my age an target audience.

Target Market(s)

Adult people, up scale audience

Industry/Entity Type

Music Download

Contact Information for Business Card

Cel (318) 5024471963 www.kelvarodun.com

Requirements
Must have
• open mind
Nice to have
• open mind
Should not have
• DJ

```html
<!DOCTYPE html>
<html lang="en">
<head>
<meta charset="utf-8">
<title>Kelvar Business Card</title>
<link href="https://fonts.googleapis.com/css2?family=Open+Sans:wght@400;700;800&display=swap" rel="stylesheet">
<style>
  :root {
    --page-bg: #e7e4df;
    --card-white: #f7f7f6;
    --card-shade: #e4e4e3;
    --ink: #2e2d2b;
    --band: #2b2a28;
    --band-text: #e9e9e9;
  }
  html, body {
    margin: 0;
    padding: 0;
    width: 1200px;
    height: 780px;
    overflow: hidden;
    background: var(--page-bg);
    font-family: "Open Sans", sans-serif;
  }
  .stage {
    width: 1200px;
    height: 780px;
    display: flex;
    align-items: center;
    justify-content: center;
    gap: 80px;
  }
  .card {
    position: relative;
    width: 370px;
    height: 640px;
    background: radial-gradient(ellipse at 50% 40%, var(--card-white) 40%, var(--card-shade) 100%);
    box-shadow: 0 10px 30px rgba(0,0,0,0.18);
    overflow: hidden;
    color: var(--ink);
  }
  .brand {
    display: flex;
    align-items: center;
    justify-content: center;
    gap: 14px;
  }
  .brand-mark {
    width: 22px;
    height: 22px;
    background: var(--ink);
  }
  .brand-name {
    font-weight: 800;
    font-size: 58px;
    letter-spacing: 2px;
    color: var(--ink);
    line-height: 1;
  }
  .card-front .brand { margin-top: 110px; }
  .identity {
    text-align: center;
    margin-top: 70px;
  }
  .identity-name {
    font-weight: 800;
    font-size: 25px;
    letter-spacing: 1.5px;
    margin: 0;
  }
  .identity-role {
    font-size: 17px;
    margin: 2px 0 0;
  }
  .contact {
    text-align: center;
    margin-top: 60px;
    font-size: 20px;
    line-height: 1.3;
  }
  .contact p { margin: 0; }
  .footer-band {
    position: absolute;
    left: 0;
    right: 0;
    bottom: 0;
    height: 112px;
    background: var(--band);
    color: var(--band-text);
    display: flex;
    align-items: center;
    font-size: 20px;
    letter-spacing: 0.5px;
  }
  .card-front .footer-band { justify-content: center; }
  .card-back .footer-band {
    height: 90px;
    justify-content: flex-end;
    padding-right: 32px;
    box-sizing: border-box;
  }
  .card-back .brand {
    position: absolute;
    top: 270px;
    left: 0;
    right: 0;
  }
  .card-back .brand-name { font-size: 64px; }
</style>
</head>
<body>
  <main class="stage">
    <section class="card card-front" aria-label="Card front">
      <div class="brand">
        <span class="brand-mark"></span>
        <span class="brand-name">KELVAR</span>
      </div>
      <div class="identity">
        <h1 class="identity-name">EMPLOYEE NAME</h1>
        <p class="identity-role">Development Manager</p>
      </div>
      <div class="contact">
        <p>(318) 5024471963</p>
        <p>mail@kelvarodun.com</p>
      </div>
      <div class="footer-band">www.kelvarodun.com</div>
    </section>

    <section class="card card-back" aria-label="Card back">
      <div class="brand">
        <span class="brand-mark"></span>
        <span class="brand-name">KELVAR</span>
      </div>
      <div class="footer-band">www.kelvarodun.com</div>
    </section>
  </main>
</body>
</html>
```